Simple self-assessment tool

I need small businesses to enter a self-assessment. The self assessment link should be found on my WP website. The app needs to come in company colors (pre defined) needs to contain 6 sections of 3 to 6 questions. the average result per section should be visible in a (radial bar chart) graph after entering the last question.
Each section should have informative picture upload possible and information button whit text if you hoover over it. The page should have a title descriptive text. The number of of answers to give per question is 1 . Answer is either, 1,2,3,4 or 5 (likert scale) each page should have a back and forth button. There should be as well a non mandatory contact form. The results of the questions can be collected in excel or google sheets for our own use. The average result graph should become visual after answering all the questions. Text that comes with it should be conditional based on the outcome of the answers. Other option is that these results are sent by email to the submitter in pdf.
Compagnies that must fulfill CSRD reporting
Sustainability for different types of compagnies, logistic service providers/ manufacturing

```html
<!DOCTYPE html>
<html lang="en">
<head>
<meta charset="UTF-8">
<title>Sustainability Self-Assessment – Section 2</title>
<link href="https://fonts.googleapis.com/css2?family=Poppins:wght@400;500;600&display=swap" rel="stylesheet">
<style>
  :root {
    --brand-green: #0a9148;
    --brand-blue: #35b1e8;
    --track-grey: #eef0f1;
    --ink: #1f2328;
    --muted: #5a6068;
    --radio-border: #8a8f95;
    --white: #ffffff;
  }
  * { box-sizing: border-box; margin: 0; padding: 0; }
  html, body { width: 1200px; height: 818px; overflow: hidden; background: var(--white); }
  body { font-family: "Poppins", sans-serif; color: var(--ink); position: relative; }

  .section-header { position: absolute; left: 0; top: 0; width: 1200px; height: 107px; }
  .section-header__band { position: absolute; left: 0; top: 0; }
  .section-title {
    position: absolute; left: 177px; top: 34px;
    font-size: 20px; font-weight: 500; color: var(--white); letter-spacing: 0.1px;
  }
  .progress { position: absolute; left: 0; top: 100px; width: 1200px; height: 7px; background: var(--track-grey); }
  .progress__fill { width: 300px; height: 100%; background: var(--brand-blue); }

  .brand-name {
    position: absolute; left: 878px; top: 31px;
    font-size: 26px; font-weight: 600; color: var(--brand-green); letter-spacing: 0.5px;
  }

  .question { position: absolute; left: 127px; width: 560px; }
  .question__text { font-size: 15px; font-weight: 500; line-height: 26px; display: flex; }
  .question__num { width: 18px; flex: none; }
  .question__hint { font-size: 13px; color: var(--muted); margin-left: 18px; line-height: 20px; }
  .scale { position: absolute; left: 19px; display: flex; }
  .scale__option { width: 65px; display: flex; flex-direction: column; align-items: center; font-size: 13px; color: var(--muted); }
  .scale__dot {
    width: 16px; height: 16px; border-radius: 50%;
    border: 1px solid var(--radio-border); margin-bottom: 4px; position: relative;
  }
  .scale__option--selected .scale__dot { border: 1.5px solid var(--brand-green); }
  .scale__option--selected .scale__dot::after {
    content: ""; position: absolute; inset: 2.5px; border-radius: 50%; background: var(--brand-green);
  }

  .q1 { top: 156px; } .q1 .scale { top: 71px; }
  .q2 { top: 309px; } .q2 .scale { top: 71px; }
  .q3 { top: 462px; } .q3 .scale { top: 94px; }

  .illustration {
    position: absolute; left: 742px; top: 158px; width: 325px; height: 334px;
    border-radius: 10px;
    background: linear-gradient(160deg, #eef6fb 0%, #cfe9f7 55%, #e9eef2 100%);
  }

  .nav-button {
    position: absolute; top: 646px; width: 119px; height: 42px;
    border: 1.5px solid var(--brand-green); border-radius: 3px; background: var(--white);
    color: var(--brand-green); font-family: "Poppins", sans-serif; font-size: 13px; font-weight: 500;
    display: flex; align-items: center; justify-content: center;
  }
  .nav-button--back { left: 125px; }
  .nav-button--next { left: 955px; }
</style>
</head>
<body>
  <header class="section-header">
    <svg class="section-header__band" width="800" height="100" viewBox="0 0 800 100" aria-hidden="true">
      <path d="M143 0 H790 L757 82 Q749 100 728 100 H123 L153 12 Q157 0 170 0 Z" fill="var(--brand-green)"/>
    </svg>
    <h1 class="section-title">2. Sustainability Policy, Strategy &amp; Governance</h1>
    <div class="brand-name">EcoPulse</div>
  </header>
  <div class="progress"><div class="progress__fill"></div></div>

  <section class="question q1">
    <p class="question__text"><span class="question__num">1.</span><span>Is there a documented sustainability policy in place in your company?</span></p>
    <div class="scale">
      <div class="scale__option"><span class="scale__dot"></span>0</div>
      <div class="scale__option"><span class="scale__dot"></span>1</div>
      <div class="scale__option"><span class="scale__dot"></span>2</div>
      <div class="scale__option"><span class="scale__dot"></span>3</div>
      <div class="scale__option scale__option--selected"><span class="scale__dot"></span>4</div>
      <div class="scale__option"><span class="scale__dot"></span>5</div>
    </div>
  </section>

  <section class="question q2">
    <p class="question__text"><span class="question__num">2.</span><span>Do all layers of the company's strategy-making process incorporate sustainability issues included as a standard for strategy setting?</span></p>
    <div class="scale">
      <div class="scale__option"><span class="scale__dot"></span>0</div>
      <div class="scale__option"><span class="scale__dot"></span>1</div>
      <div class="scale__option"><span class="scale__dot"></span>2</div>
      <div class="scale__option"><span class="scale__dot"></span>3</div>
      <div class="scale__option scale__option--selected"><span class="scale__dot"></span>4</div>
      <div class="scale__option"><span class="scale__dot"></span>5</div>
    </div>
  </section>

  <section class="question q3">
    <p class="question__text"><span class="question__num">3.</span><span>Are the sustainability objectives in the strategy future-proof or is the focus on short-term goals?</span></p>
    <p class="question__hint">(short-term goals - 0, long-term strategy - 5)</p>
    <div class="scale">
      <div class="scale__option"><span class="scale__dot"></span>0</div>
      <div class="scale__option"><span class="scale__dot"></span>1</div>
      <div class="scale__option"><span class="scale__dot"></span>2</div>
      <div class="scale__option"><span class="scale__dot"></span>3</div>
      <div class="scale__option scale__option--selected"><span class="scale__dot"></span>4</div>
      <div class="scale__option"><span class="scale__dot"></span>5</div>
    </div>
  </section>

  <div class="illustration" role="img" aria-label="Illustration of a woman with a tablet beside a checklist clipboard, stopwatch, gears and a stack of books"></div>

  <a class="nav-button nav-button--back">Back</a>
  <a class="nav-button nav-button--next">Next</a>
</body>
</html>
```